Vodka label for New Brand called KIRO Vodka

We need a label measuring 3.5 inches wide & 5 inches tall for this vodka bottle. The brand is "KIRO Vodka". This should be the largest font on the label. "Handcrafted in the USA" should be on bottle in small font near the bottom. The tagline "Keeping It Real Onward" also needs to be included anywhere that makes sense in a smaller font than the brand name. Also in smaller font at the bottom/corners- "80 proof, 750 ml, 40% alc/vol" I value the human mind over AI, but am providing a couple designs that were AI generated to give you a better idea where to start and what we are looking for. Thank you!

Target Market(s)

21-45 year olds.

Industry/Entity Type

Alcohol

Colors
0054AA
0677BA
7BADD7
CADEEF
E8F1F8
EB3D1F
EC4F4E
F09395
F8D3D4
FCEDEE

Requirements
Should not have
• You can not use the US flag but can use elements of it.

```html
<!DOCTYPE html>
<html lang="en">
<head>
<meta charset="utf-8">
<title>KIRO Vodka Label</title>
<link rel="stylesheet" href="https://fonts.googleapis.com/css2?family=Big+Shoulders+Display:wght@900&family=Montserrat:wght@600;800&family=Allura&family=Oswald:wght@300&display=swap">
<style>
  :root {
    --label-bg: #ffffff;
    --brand-blue: #233c98;
    --accent-red: #eb3d1f;
    --ink: #000000;
  }
  html, body {
    margin: 0;
    padding: 0;
    overflow: hidden;
    background: var(--label-bg);
  }
  .label {
    position: relative;
    width: 840px;
    height: 1200px;
    overflow: hidden;
    background: var(--label-bg);
  }
  .wordmark {
    position: absolute;
    left: 0;
    top: 0;
  }
  .wordmark__name {
    font-family: "Big Shoulders Display", "Oswald", sans-serif;
    font-weight: 900;
    fill: var(--brand-blue);
  }
  .wordmark__tagline {
    font-family: "Montserrat", sans-serif;
    font-weight: 600;
    font-size: 29px;
    letter-spacing: 0.32em;
    fill: var(--accent-red);
  }
  .product-type {
    position: absolute;
    left: 0;
    width: 840px;
    top: 888px;
    margin: 0;
    text-align: center;
    font-family: "Montserrat", sans-serif;
    font-weight: 800;
    font-size: 72px;
    line-height: 1;
    letter-spacing: 0.12em;
    padding-left: 0.12em;
    box-sizing: border-box;
    color: var(--ink);
  }
  .origin-stripes {
    position: absolute;
    top: 1000px;
    width: 212px;
    height: 41px;
  }
  .origin-stripes--left { left: 0; }
  .origin-stripes--right { right: 0; }
  .origin-stripes span {
    position: absolute;
    left: 0;
    width: 100%;
    height: 7px;
  }
  .origin-stripes .stripe-blue { top: 3px; background: var(--brand-blue); }
  .origin-stripes .stripe-red-1 { top: 18px; background: var(--accent-red); }
  .origin-stripes .stripe-red-2 { top: 33px; background: var(--accent-red); }
  .origin {
    position: absolute;
    left: 0;
    width: 840px;
    top: 968px;
    margin: 0;
    text-align: center;
    color: var(--ink);
  }
  .origin__script {
    display: block;
    font-family: "Allura", cursive;
    font-size: 78px;
    line-height: 1;
  }
  .origin__country {
    display: block;
    margin-top: -6px;
    font-family: "Montserrat", sans-serif;
    font-weight: 600;
    font-size: 25px;
    letter-spacing: 0.22em;
    padding-left: 0.22em;
  }
  .spec-line {
    position: absolute;
    left: 0;
    width: 840px;
    top: 1122px;
    margin: 0;
    text-align: center;
    font-family: "Oswald", sans-serif;
    font-weight: 300;
    font-size: 27px;
    letter-spacing: 0.16em;
    padding-left: 0.16em;
    box-sizing: border-box;
    color: var(--ink);
  }
</style>
</head>
<body>
  <main class="label">
    <svg class="wordmark" width="840" height="880" viewBox="0 0 840 880" aria-label="KIRO — Keeping It Real Onward">
      <g transform="scale(1,5.5)">
        <text class="wordmark__name" x="30" y="156.5" font-size="200" textLength="778" lengthAdjust="spacingAndGlyphs">KIRO</text>
      </g>
      <text class="wordmark__tagline" transform="translate(66,288) rotate(-90)">KEEPING</text>
      <text class="wordmark__tagline" transform="translate(272,480) rotate(-90)">IT</text>
      <text class="wordmark__tagline" transform="translate(450,610) rotate(-90)">REAL</text>
      <text class="wordmark__tagline" transform="translate(796,822) rotate(-90)">ONWARD.</text>
    </svg>

    <h1 class="product-type">VODKA</h1>

    <div class="origin-stripes origin-stripes--left" aria-hidden="true">
      <span class="stripe-blue"></span><span class="stripe-red-1"></span><span class="stripe-red-2"></span>
    </div>
    <div class="origin-stripes origin-stripes--right" aria-hidden="true">
      <span class="stripe-blue"></span><span class="stripe-red-1"></span><span class="stripe-red-2"></span>
    </div>

    <p class="origin">
      <span class="origin__script">Handcrafted</span>
      <span class="origin__country">IN THE USA</span>
    </p>

    <p class="spec-line">80 PROOF, 750 ML, 40% ALC/VOL</p>
  </main>
</body>
</html>
```